Full cover (front, back and side of the book). 28 cm x 20 cm total (High 20 cm, width 13, side 2 cm) Front cover: Title of the author on top, centered (Mathieu Clavreux) Title: Counting the rivers Subtitle: Sailing keeper coastal Bottom and centered: attached logo (Vorelma Editions) in white, and edited eventualy. Side: From left to right: Editor logo (only "Vorelma" word, without the "Editions" word, title and author name Back cover: Left text column ) Bottom: space available for the bar coded price and 2 or 3 lines of text Right text column (approx 6.5 cm wide) Bottom of the right colum, center of the right column: same attached logo (Vorelma Editions) in white, and edited eventualy, with www.vorelma.example below the logo. Left Lateral margin of the back cover, this book should be almost 1 cm)
Colors
Designer to choose colors to be used in the design.

```html
<!DOCTYPE html>
<html lang="en">
<head>
<meta charset="utf-8">
<title>Counting the Rivers – Full Cover</title>
<link rel="stylesheet" href="https://fonts.googleapis.com/css2?family=Montserrat:wght@600;700&family=Didact+Gothic&display=swap">
<style>
  :root {
    --stage: #000000;
    --navy: #173a5e;
    --spine-band: #24486b;
    --column-blue: #1d7fb4;
    --ink: #14304c;
    --white: #ffffff;
    --sky-deep: #2f93c9;
    --sky-light: #d6ebf5;
    --island: #2f5d4c;
    --lagoon: #1f9fb8;
    --shallows: #62d2d6;
  }
  * { margin: 0; padding: 0; box-sizing: border-box; }
  html, body { width: 1200px; height: 857px; overflow: hidden; background: var(--stage); }
  .canvas { position: relative; width: 1200px; height: 857px; }

  .cover { position: absolute; left: 98px; top: 70px; width: 1004px; height: 716px; }

  .panel { position: absolute; top: 0; height: 716px; overflow: hidden; }
  .back { left: 0; width: 467px; }
  .spine { left: 467px; width: 71px; }
  .front { left: 538px; width: 466px; }

  .scenery {
    position: absolute; inset: 0;
    background: linear-gradient(180deg,
      var(--sky-deep) 0%, var(--sky-light) 18%, #9fd0ea 34%, #5eb0dc 52%,
      var(--island) 58%, #3d7a66 62%, var(--lagoon) 68%, #25b0c2 82%, var(--shallows) 100%);
  }
  .back .scenery {
    background:
      linear-gradient(90deg, rgba(255,255,255,0.55) 0%, rgba(255,255,255,0.75) 40%, rgba(255,255,255,0.35) 70%, rgba(255,255,255,0) 100%),
      linear-gradient(180deg, var(--sky-deep) 0%, var(--sky-light) 20%, #bfe0f0 50%, #7cc3dc 70%, #33b2c4 85%, var(--shallows) 100%);
  }
  .spine .scenery {
    background: linear-gradient(180deg, #5ab1dc 0%, #d2e9f3 25%, #a9d4e8 50%, #4aa8cc 75%, #2b9fbb 100%);
  }

  .heading-font { font-family: "Montserrat", sans-serif; }
  .text-font { font-family: "Didact Gothic", sans-serif; }

  /* Front */
  .front-author {
    position: absolute; top: 62px; left: 0; width: 100%; text-align: center;
    font-family: "Montserrat", sans-serif; font-weight: 600; font-size: 29px;
    color: var(--navy); letter-spacing: 0.5px;
    text-shadow: 0 0 8px rgba(255,255,255,0.8);
  }
  .front-title {
    position: absolute; top: 200px; left: 0; width: 100%; text-align: center;
    color: var(--navy); font-family: "Montserrat", sans-serif; font-weight: 700;
    text-shadow: 0 0 10px rgba(255,255,255,0.85);
    line-height: 1;
  }
  .front-title .line-one { display: block; font-size: 62px; letter-spacing: 1px; }
  .front-title .line-two { display: block; margin-top: 10px; font-size: 76px; }
  .front-title .small-the { font-size: 36px; margin-right: 6px; }
  .front-subtitle {
    position: absolute; top: 372px; left: 0; width: 100%; text-align: center;
    font-family: "Didact Gothic", sans-serif; font-size: 30px; color: var(--navy);
    letter-spacing: 0.5px; text-shadow: 0 0 8px rgba(255,255,255,0.85);
  }

  .imprint {
    position: absolute; text-align: center; color: var(--white);
    font-family: "Montserrat", sans-serif; font-weight: 700;
  }
  .front .imprint { left: 0; width: 100%; top: 650px; font-size: 20px; line-height: 1.1; }
  .imprint .word { display: block; }
  .imprint .word-small { font-size: 13px; }

  /* Back */
  .back-title {
    position: absolute; left: 256px; top: 50px; width: 144px; text-align: right;
    font-family: "Montserrat", sans-serif; font-weight: 700; color: var(--navy); line-height: 1;
  }
  .back-title .line-one { display: block; font-size: 20px; text-align: center; }
  .back-title .line-two { display: block; font-size: 25px; margin-top: 4px; text-align: center; }
  .back-title .small-the { font-size: 14px; }
  .back-title .subtitle {
    display: block; font-family: "Didact Gothic", sans-serif; font-weight: 400;
    font-size: 10.5px; margin-top: 2px; text-align: center;
  }

  .column-left {
    position: absolute; left: 31px; top: 134px; width: 162px;
    font-family: "Didact Gothic", sans-serif; font-size: 12.2px; line-height: 15.2px;
    color: var(--column-blue); text-align: justify;
  }
  .column-right {
    position: absolute; left: 212px; top: 134px; width: 228px;
    font-family: "Didact Gothic", sans-serif; font-size: 13.8px; line-height: 17.5px;
    color: var(--ink); text-align: justify;
  }
  .column-left p, .column-right p { text-indent: 1em; }
  .column-left p + p { margin-top: 15px; }
  .column-right p + p { margin-top: 17px; }

  .back .imprint { left: 230px; width: 190px; top: 598px; font-size: 18px; line-height: 1.1; }
  .back-url {
    position: absolute; left: 230px; width: 190px; top: 641px; text-align: center;
    font-family: "Didact Gothic", sans-serif; font-size: 11.5px; color: var(--white);
  }

  /* Spine */
  .spine-text {
    position: absolute; writing-mode: vertical-rl; transform: rotate(180deg);
    color: var(--navy); white-space: nowrap;
  }
  .spine-author {
    left: 22px; top: 50px; height: 226px; width: 28px;
    font-family: "Montserrat", sans-serif; font-weight: 700; font-size: 20px;
    letter-spacing: 1.2px; text-align: end;
  }
  .spine-title {
    left: 8px; top: 300px; height: 338px; width: 34px;
    font-family: "Montserrat", sans-serif; font-weight: 700; font-size: 27px;
    letter-spacing: 0.3px;
  }
  .spine-subtitle {
    left: 38px; top: 300px; height: 310px; width: 26px;
    font-family: "Didact Gothic", sans-serif; font-size: 20px;
  }
  .spine-band {
    position: absolute; left: 0; bottom: 0; width: 100%; height: 58px;
    background: var(--spine-band); display: flex; align-items: center; justify-content: center;
    font-family: "Montserrat", sans-serif; font-weight: 700; font-size: 13px; color: var(--white);
  }
</style>
</head>
<body>
<div class="canvas">
  <div class="cover">

    <section class="panel back">
      <div class="scenery" role="img" aria-label="Photo of a light aircraft flying over a turquoise lagoon under a cloudy sky, faded behind the text"></div>
      <div class="back-title">
        <span class="line-one">COUNTING</span>
        <span class="line-two"><span class="small-the">THE</span> RIVERS</span>
        <span class="subtitle">SAILING KEEPER COASTAL</span>
      </div>
      <div class="column-left">
        <p>Lorem ipsum dolor sit amet, consectetur adipiscing elit. Duis id augue ornare, tincidunt dolor sit amet, tincidunt tortor. Sed dignissim consequat ante, eget vehicula orci dapibus quis.</p>
        <p>Quisque congue viverra tellus, id sollicitudin magna blandit a. Nunc dignissim nibh nisi. Aenean fermentum dolor a lectus volutpat, quis vestibulum lacus semper. Phasellus interdum ante a semper varius. Sed nec arcu justo. Phasellus congue sem quis dictum cursus.</p>
      </div>
      <div class="column-right">
        <p>Cras risus lorem, dapibus a scelerisque in, eleifend at arcu. In sagittis erat ut volutpat consequat. Quisque lectus lectus, aliquet eget nunc id, rhoncus commodo est. Fusce id felis mattis, consectetur ante non, eleifend metus. Nunc euismod eget sapien eget dapibus. Duis eget commodo dui, ut varius sapien.</p>
        <p>Aliquam erat volutpat. Etiam semper ex ut orci laoreet, nec vestibulum orci iaculis. Duis rutrum tincidunt diam, ac venenatis turpis tristique et. Proin at nunc quis velit aliquam elementum porttitor at est. Proin congue diam neque, id faucibus sapien faucibus a. Pellentesque a leo lorem.</p>
      </div>
      <div class="imprint">
        <span class="word word-small">EDITIONS</span>
        <span class="word">VORELMA</span>
      </div>
      <div class="back-url">www.vorelma.example</div>
    </section>

    <section class="panel spine">
      <div class="scenery" role="img" aria-label="Soft sky-to-sea colour wash along the spine"></div>
      <div class="spine-text spine-author">MATHIEU CLAVREUX</div>
      <div class="spine-text spine-title">COUNTING THE RIVERS</div>
      <div class="spine-text spine-subtitle">SAILING KEEPER COASTAL</div>
      <div class="spine-band">VORELMA</div>
    </section>

    <section class="panel front">
      <div class="scenery" role="img" aria-label="Photo of a light aircraft flying over a turquoise lagoon with a green island and clouds above"></div>
      <div class="front-author">MATHIEU CLAVREUX</div>
      <h1 class="front-title">
        <span class="line-one">COUNTING</span>
        <span class="line-two"><span class="small-the">THE</span>RIVERS</span>
      </h1>
      <div class="front-subtitle">SAILING KEEPER COASTAL</div>
      <div class="imprint">
        <span class="word word-small">EDITIONS</span>
        <span class="word">VORELMA</span>
      </div>
    </section>

  </div>
</div>
</body>
</html>
```